LOMADRIS COFFEE CUPS

I WANT A DESIGN FOR TAKE AWAY COFFEE CUPS 12 oz. IN THE ATTACHED PROFILES YOU'LL FIND THE LOGO AND SOME DESIGNS I LIKE (WHICH IS FLOWER OR COFFEE QOUTES) THE COLORS ARE PREFERLY WHITE, PINK, PURPLE OR YOU CAN DO OTHER COLORS IF NICER.

```html
<!DOCTYPE html>
<html lang="en">
<head>
<meta charset="utf-8">
<title>Lomadris Coffee Cup Wrap</title>
<link rel="stylesheet" href="https://fonts.googleapis.com/css2?family=Dancing+Script:wght@500&family=Open+Sans:wght@400;600&display=swap">
<style>
  :root {
    --page: #ffffff;
    --wrap-blue: #4f5499;
    --ink: #ffffff;
    --pink: #e48aa6;
    --pink-light: #f6c9d6;
    --violet: #9b7fcf;
    --violet-light: #d9c6f0;
    --petal-white: #f3f0f4;
  }
  * { margin: 0; padding: 0; box-sizing: border-box; }
  html, body {
    width: 1200px; height: 1200px; overflow: hidden;
    background: var(--page);
  }
  .cup-wrap {
    position: absolute; left: 45px; top: 324px;
    width: 1110px; height: 552px;
    background: var(--wrap-blue);
    overflow: hidden;
  }
  .flower {
    position: absolute; border-radius: 50%;
    filter: blur(2px);
  }
  .flower--pink-peony {
    left: -40px; top: 300px; width: 330px; height: 300px;
    background: radial-gradient(circle at 45% 45%, var(--pink-light), var(--pink) 55%, #c9708f 100%);
  }
  .flower--violet-peony {
    left: 330px; top: 335px; width: 280px; height: 260px;
    background: radial-gradient(circle at 50% 45%, var(--violet-light), var(--violet) 60%, #7c63b3 100%);
  }
  .flower--white-bloom {
    left: 645px; top: 318px; width: 190px; height: 215px;
    background: radial-gradient(circle at 50% 45%, #ffffff, var(--petal-white) 55%, #d6d0dc 100%);
  }
  .flower--top-pink {
    left: 495px; top: -60px; width: 200px; height: 150px;
    background: radial-gradient(circle at 50% 60%, var(--pink-light), var(--pink) 70%);
  }
  .flower--top-white {
    left: 690px; top: -60px; width: 140px; height: 120px;
    background: radial-gradient(circle at 50% 60%, #ffffff, var(--petal-white) 70%);
  }
  .flower--top-violet {
    left: 835px; top: -55px; width: 175px; height: 140px;
    background: radial-gradient(circle at 50% 60%, var(--violet-light), var(--violet) 75%);
  }
  .quote {
    position: absolute; left: 100px; top: 40px; width: 240px;
    color: var(--ink);
    font-family: "Dancing Script", cursive;
    font-size: 42px; line-height: 1;
    text-align: center;
  }
  .quote__mark { display: block; font-size: 60px; height: 36px; margin-bottom: 12px; padding-left: 30px; }
  .quote__line { display: block; margin-bottom: 14px; }
  .quote__tilde { display: block; font-size: 30px; height: 18px; margin-top: -10px; }
  .brand {
    position: absolute; left: 415px; top: 185px;
    color: var(--ink);
    font-family: "Open Sans", sans-serif;
    font-weight: 600; font-size: 64px; letter-spacing: 1px;
  }
  .order-list {
    position: absolute; left: 850px; top: 288px;
    list-style: none;
    color: var(--ink);
    font-family: "Open Sans", sans-serif;
    font-size: 21px; letter-spacing: 0.5px;
  }
  .order-list__item { display: flex; align-items: center; height: 43px; }
  .order-list__box {
    width: 29px; height: 29px; border: 1.5px solid var(--ink);
    margin-right: 18px;
  }
</style>
</head>
<body>
  <section class="cup-wrap">
    <div class="flower flower--top-pink" role="img" aria-label="Pink peony petals along the top edge"></div>
    <div class="flower flower--top-white" role="img" aria-label="White peony petals along the top edge"></div>
    <div class="flower flower--top-violet" role="img" aria-label="Lilac peony petals along the top edge"></div>
    <div class="flower flower--pink-peony" role="img" aria-label="Large pink peony illustration"></div>
    <div class="flower flower--violet-peony" role="img" aria-label="Purple peony illustration"></div>
    <div class="flower flower--white-bloom" role="img" aria-label="White carnation illustration"></div>

    <p class="quote">
      <span class="quote__mark">”</span>
      <span class="quote__line">You call it</span>
      <span class="quote__line">addiction</span>
      <span class="quote__tilde">~</span>
      <span class="quote__line">I prefer</span>
      <span class="quote__line">love</span>
    </p>

    <h1 class="brand">LOMADRIS</h1>

    <ul class="order-list">
      <li class="order-list__item"><span class="order-list__box"></span>Cafe Latté</li>
      <li class="order-list__item"><span class="order-list__box"></span>Capuchino</li>
      <li class="order-list__item"><span class="order-list__box"></span>Americano</li>
      <li class="order-list__item"><span class="order-list__box"></span>Cafe Mocha</li>
      <li class="order-list__item"><span class="order-list__box"></span>ETC</li>
    </ul>
  </section>
</body>
</html>
```